I am writing a book called "SMILING OPENS EVERY DOOR "

I NEED A BOOK COVER FOR MY BOOK" SMILING OPENS EVERY DOOR"
so what was the question? " ( this in smaller font)

"Smiling Opens Every Door " will need to designed to eventually be a logo , banner and business card
COLOURS MAINLY ORANGE AND WHITE (with accents bright colour )

THE BOOK IS MY LAUGHTER JOURNEY AS A PERFORMER AND ADVENTURE INDIA LEARNING ABOUT LAUGHTER YOGA WHICH I WILL BE TEACHING

I do not want photos on the front cover ..
The look could be modern and eye-catching
I have also just been to India to learn Laughing Yoga with Dr Tobin Verhaal

Thank-you so much everyone for your brilliant designs . i am overwhelmed with your talent . i hope to work with you all again soon ! Marnie  

Target Market(s)

"Adults based in western speaking countries aged 25 to 60 that want to learn to laugh more
Also this book will be sold at my conference workshops

Industry/Entity Type

Business

Requirements
Must have
• ORANGE AND WHITE
CAN HAVE AQUA , HOT PINK , LIME GREEN, YELLOW ACCENTS

THESE WILL BE DIFFERENT AREAS WILL COVERING IN MY BOOK
EG LAUGHTER NAD BREAT CANCER ( PINK)
LAUGHTER NAD DEPRESSION ( BLUE)
LAUGHTER AND KIDS ( YELLOW)

NO Photos on front cover
Should not have
• No photos

```html
<!DOCTYPE html>
<html lang="en">
<head>
<meta charset="utf-8">
<title>Smiling Opens Every Door – Book Cover</title>
<link rel="stylesheet" href="https://fonts.googleapis.com/css2?family=Titan+One&family=Courgette&family=Arimo:wght@700&display=swap">
<style>
  :root {
    --backdrop: #ececec;
    --paper: #ffffff;
    --orange: #e8561a;
    --title-fill: #fbe3cf;
    --title-edge: #e0701e;
    --ink: #1b1b1b;
    --art-top: #fde2cc;
    --art-mid: #fbd0bf;
    --art-low: #f7e7ee;
  }
  * { margin: 0; padding: 0; box-sizing: border-box; }
  html, body { width: 1200px; height: 800px; overflow: hidden; }
  body {
    background: var(--backdrop);
    display: flex;
    align-items: center;
    justify-content: center;
  }
  .book-wrap {
    display: flex;
    width: 850px;
    height: 620px;
    box-shadow: 0 12px 30px rgba(0,0,0,0.12);
  }

  .title {
    font-family: "Titan One", sans-serif;
    color: var(--title-fill);
    text-align: center;
    line-height: 1.1;
    text-shadow:
      -2px -2px 0 var(--title-edge), 2px -2px 0 var(--title-edge),
      -2px 2px 0 var(--title-edge), 2px 2px 0 var(--title-edge),
      0 4px 5px rgba(120,50,10,0.3);
  }

  /* ---------- back cover ---------- */
  .back-cover {
    position: relative;
    width: 410px;
    height: 100%;
    background: var(--paper);
    padding: 18px 34px 0;
  }
  .back-author {
    text-align: right;
    padding-right: 30px;
    font-family: "Courgette", cursive;
    font-size: 15px;
    color: var(--orange);
  }
  .back-title { font-size: 31px; margin-top: 4px; }
  .blurb {
    margin-top: 14px;
    font-family: "Arimo", Arial, sans-serif;
    font-weight: 700;
    font-size: 11.5px;
    line-height: 1.35;
    color: var(--ink);
    text-align: justify;
    text-align-last: center;
  }
  .back-boxes {
    position: absolute;
    left: 34px;
    right: 34px;
    bottom: 28px;
    display: flex;
    justify-content: space-between;
  }
  .back-box {
    width: 120px;
    height: 50px;
    background: var(--orange);
    color: var(--paper);
    font-family: "Arimo", Arial, sans-serif;
    font-size: 10px;
    display: flex;
    align-items: center;
    justify-content: center;
  }

  /* ---------- spine ---------- */
  .spine {
    width: 30px;
    height: 100%;
    background: linear-gradient(90deg, #f3f3f3, #ffffff 50%, #eaeaea);
    display: flex;
    flex-direction: column;
    align-items: center;
    padding-top: 20px;
  }
  .spine-title {
    writing-mode: vertical-rl;
    font-family: "Titan One", sans-serif;
    font-size: 19px;
    color: var(--title-fill);
    text-shadow:
      -1px -1px 0 var(--title-edge), 1px -1px 0 var(--title-edge),
      -1px 1px 0 var(--title-edge), 1px 1px 0 var(--title-edge);
  }
  .spine-author {
    writing-mode: vertical-rl;
    margin-top: 16px;
    font-family: "Courgette", cursive;
    font-size: 9px;
    color: var(--orange);
  }

  /* ---------- front cover ---------- */
  .front-cover {
    position: relative;
    width: 410px;
    height: 100%;
    background: var(--paper);
    overflow: hidden;
  }
  .front-heading {
    position: absolute;
    top: 22px; left: 0; right: 0;
  }
  .front-title { font-size: 38px; }
  .subtitle {
    margin-top: 8px;
    text-align: center;
    font-family: "Courgette", cursive;
    font-size: 17px;
    color: var(--orange);
  }
  .cover-art {
    position: absolute;
    left: 85px;
    top: 200px;
    width: 240px;
    height: 340px;
    border-radius: 50%;
    background: radial-gradient(ellipse at 50% 45%, var(--art-top) 0%, var(--art-mid) 50%, var(--art-low) 100%);
  }
  .author-band {
    position: absolute;
    left: 0; right: 0; bottom: 0;
    height: 52px;
    background: var(--orange);
    display: flex;
    align-items: center;
    justify-content: center;
    font-family: "Courgette", cursive;
    font-size: 20px;
    color: var(--paper);
  }
</style>
</head>
<body>
  <main class="book-wrap">
    <section class="back-cover">
      <p class="back-author">Author Name</p>
      <h2 class="title back-title">SMILING OPENS<br>EVERY DOOR</h2>
      <p class="blurb">Marnie has spent twenty years on stage making crowds giggle, roar and sometimes cry with joy. Then one trip to India changed everything. In this warm and honest book she shares her own laughter journey, from comedy clubs and street shows to sunrise sessions of laughter yoga in busy city parks. Along the way she met Dr Tobin Verhaal and learned that laughing for no reason at all can lift the mood, ease stress and bring strangers together in minutes. Each chapter looks at laughter in a new part of life: laughter and breast cancer, laughter and depression, laughter and kids, laughter at work and laughter at home. You will find simple exercises you can try today, true stories from people who found their smile again, and practical tips for bringing more play into every single day. Whether you want to lead a laughter club, calm a noisy classroom or simply feel lighter, this book will show you how. You do not need a joke, a reason or a good day to begin. You only need to breathe, open your mouth and let it out. So what was the question? The answer has been waiting inside you all along. Turn the page, take a deep breath and start smiling.</p>
      <div class="back-boxes">
        <div class="back-box">LOGO</div>
        <div class="back-box">ISBN</div>
      </div>
    </section>

    <section class="spine">
      <span class="spine-title">SMILING OPENS EVERY DOOR</span>
      <span class="spine-author">Author Name</span>
    </section>

    <section class="front-cover">
      <div class="front-heading">
        <h1 class="title front-title">SMILING OPENS<br>EVERY DOOR</h1>
        <p class="subtitle">so what was the question?</p>
      </div>
      <div class="cover-art" role="img" aria-label="Soft cover artwork area in warm peach and pink tones"></div>
      <div class="author-band">Author Name</div>
    </section>
  </main>
</body>
</html>
```